Business Card Design

I need a Business Card that will catch the attention that will not get thrown in a Drawer. I have 23 companies I use for Auto, Home, Life, and Business Insurance. I make sure that people have the best coverage for the $ spent.

Industry/Entity Type

Business

Contact Information for Business Card

Dorlin Insurance Agency, Inc., Marcus Helgren, 4375 West Tamber Lane Brackwood, Idaho 45192 555-281-7496, www.dorlinagency.example, Facebook, LinkedIn, Google+

```html
<!DOCTYPE html>
<html lang="en">
<head>
<meta charset="utf-8">
<title>Dorlin Insurance Agency – Business Cards</title>
<link rel="stylesheet" href="https://fonts.googleapis.com/css2?family=Arimo:wght@700&family=Open+Sans:wght@400;600&display=swap">
<style>
  :root {
    --backdrop: #e4e4e4;
    --card: #ffffff;
    --teal: #2aa0b9;
    --navy: #0e4a8a;
    --ink: #1f1f1f;
    --on-navy: #ffffff;
  }
  * { box-sizing: border-box; margin: 0; padding: 0; }
  html, body { width: 1200px; height: 750px; overflow: hidden; }
  body {
    background: var(--backdrop);
    font-family: "Open Sans", Arial, sans-serif;
    position: relative;
  }
  .card {
    position: absolute;
    top: 232px;
    width: 500px;
    height: 286px;
    background: var(--card);
    border-radius: 18px;
    overflow: hidden;
    box-shadow: 0 2px 6px rgba(0,0,0,0.12);
  }
  .card--stacked { left: 60px; }
  .card--banner { left: 640px; }

  .side-band {
    position: absolute;
    left: 0; top: 0; bottom: 0;
    width: 40px;
    background: var(--teal);
    display: flex;
    align-items: center;
    justify-content: center;
  }
  .side-band__url {
    writing-mode: vertical-rl;
    color: var(--on-navy);
    font-size: 13px;
    letter-spacing: 0.2px;
    white-space: nowrap;
  }

  .agency {
    position: absolute;
    font-family: "Arimo", Arial, sans-serif;
    font-weight: 700;
    font-size: 19px;
    color: var(--ink);
    white-space: nowrap;
  }
  .person {
    position: absolute;
    font-family: "Open Sans", Arial, sans-serif;
    color: var(--ink);
    white-space: nowrap;
  }
  .person .initial { color: var(--navy); font-weight: 600; }

  .contact-panel {
    position: absolute;
    background: var(--navy);
    color: var(--on-navy);
    font-size: 14px;
    line-height: 1.35;
    white-space: nowrap;
  }
  .contact-panel__phone { font-size: 15px; margin-bottom: 2px; }

  .icons {
    position: absolute;
    display: flex;
    flex-direction: column;
    gap: 8px;
  }
  .icons svg { display: block; width: 20px; height: 20px; }

  /* Stacked card */
  .card--stacked .agency { left: 66px; top: 62px; }
  .card--stacked .top-rule {
    position: absolute;
    top: 90px; left: 66px; right: 0;
    height: 2px;
    background: var(--teal);
  }
  .card--stacked .person { left: 250px; top: 102px; font-size: 19px; }
  .card--stacked .contact-panel {
    left: 212px; right: 22px; top: 140px; height: 112px;
    border-radius: 22px;
    padding: 30px 0 0 24px;
  }
  .card--stacked .icons { left: 182px; top: 196px; }

  /* Banner card */
  .card--banner .agency { left: 0; right: 0; top: 34px; text-align: center; padding-left: 40px; }
  .card--banner .contact-panel {
    left: 262px; right: 0; top: 76px; height: 98px;
    border-radius: 18px 0 0 18px;
    padding: 14px 0 0 22px;
  }
  .card--banner .icons { left: 232px; top: 112px; }
  .card--banner .person { left: 66px; top: 196px; font-size: 25px; }
</style>
</head>
<body>

<section class="card card--stacked" aria-label="Business card, stacked layout">
  <div class="side-band"><span class="side-band__url">www.dorlinagency.example</span></div>
  <h1 class="agency">Dorlin Insurance Agency</h1>
  <div class="top-rule"></div>
  <p class="person"><span class="initial">M</span>arcus <span class="initial">H</span>elgren</p>
  <div class="icons">
    <svg viewBox="0 0 20 20" aria-label="Phone"><circle cx="10" cy="10" r="9" fill="var(--navy)"/><rect x="6.5" y="5" width="7" height="10" rx="1.5" fill="#fff"/><rect x="8" y="6.5" width="4" height="5" fill="var(--navy)"/></svg>
    <svg viewBox="0 0 20 20" aria-label="Address"><circle cx="10" cy="10" r="9" fill="var(--navy)"/><path d="M10 4.5a3.5 3.5 0 0 0-3.5 3.5c0 2.6 3.5 7 3.5 7s3.5-4.4 3.5-7A3.5 3.5 0 0 0 10 4.5z" fill="#fff"/><circle cx="10" cy="8" r="1.3" fill="var(--navy)"/></svg>
  </div>
  <div class="contact-panel">
    <p class="contact-panel__phone">555-281-7496</p>
    <p>4375 West Tamber Lane</p>
    <p>Brackwood, Idaho 45192</p>
  </div>
</section>

<section class="card card--banner" aria-label="Business card, banner layout">
  <div class="side-band"><span class="side-band__url">www.dorlinagency.example</span></div>
  <h1 class="agency">Dorlin Insurance Agency</h1>
  <div class="icons">
    <svg viewBox="0 0 20 20" aria-label="Phone"><circle cx="10" cy="10" r="9" fill="var(--navy)"/><rect x="6.5" y="5" width="7" height="10" rx="1.5" fill="#fff"/><rect x="8" y="6.5" width="4" height="5" fill="var(--navy)"/></svg>
    <svg viewBox="0 0 20 20" aria-label="Address"><circle cx="10" cy="10" r="9" fill="var(--navy)"/><path d="M10 4.5a3.5 3.5 0 0 0-3.5 3.5c0 2.6 3.5 7 3.5 7s3.5-4.4 3.5-7A3.5 3.5 0 0 0 10 4.5z" fill="#fff"/><circle cx="10" cy="8" r="1.3" fill="var(--navy)"/></svg>
  </div>
  <div class="contact-panel">
    <p class="contact-panel__phone">555-281-7496</p>
    <p>4375 West Tamber Lane</p>
    <p>Brackwood, Idaho 45192</p>
  </div>
  <p class="person"><span class="initial">M</span>arcus <span class="initial">H</span>elgren</p>
</section>

</body>
</html>
```